Quillmark Select

Letter Head, Envelope, Business Cards, Social Media Banner (FB/Twitter), Social Media Icon, Social Media Announcement Template...

We are a Softball Team/Organization

Target Market(s)

High School Student-Athletes (softball players) and their parents

Font styles to use
Serif

Requirements
Must have
• Logo & Colors
Must POP and say WOW
Common theme amongst all designs

```html
<!DOCTYPE html>
<html lang="en">
<head>
<meta charset="utf-8">
<title>Quillmark Select – Stationery Set</title>
<link href="https://fonts.googleapis.com/css2?family=Lato:wght@400;700&family=Open+Sans:wght@400;600&display=swap" rel="stylesheet">
<style>
  :root{
    --navy:#1e3766;
    --ink:#3b3b3b;
    --muted:#5a5a5a;
    --paper:#ffffff;
    --backdrop:#dcdcdc;
    --label:#8a8a8a;
    --shadow:rgba(0,0,0,.28);
    --sig:#cfd3da;
  }
  *{margin:0;padding:0;box-sizing:border-box}
  html,body{width:1200px;height:769px;overflow:hidden}
  body{background:var(--backdrop);position:relative;font-family:"Open Sans",sans-serif;color:var(--ink)}
  .sheet{position:absolute;background:var(--paper);box-shadow:1px 2px 4px var(--shadow)}
  .wordmark{font-family:"Lato",sans-serif;font-weight:700;color:var(--navy);display:flex;align-items:center;gap:6px;white-space:nowrap;letter-spacing:.5px}
  .wordmark .dot{width:10px;height:10px;border-radius:50%;background:var(--navy);flex:none}

  /* Letterhead */
  .letterhead{left:87px;top:100px;width:437px;height:560px}
  .letterhead .wordmark{position:absolute;left:0;right:0;top:36px;justify-content:center;font-size:22px}
  .letter-body{position:absolute;left:41px;width:354px;font-size:7.1px;line-height:12.6px;color:var(--muted)}
  .letter-meta{top:100px}
  .letter-meta p{margin-bottom:8px;line-height:8.5px}
  .letter-meta .salutation{margin-top:24px}
  .letter-text{top:190px}
  .letter-text p{text-align:justify;margin-bottom:12.6px}
  .closing{position:absolute;left:41px;top:380px;font-size:7.3px;color:var(--muted)}
  .signature{display:block;width:100px;height:14px;background:var(--sig);margin:9px 0 8px;border-radius:2px}
  .signer-name{font-size:9px;font-weight:600;color:var(--ink);line-height:12px}
  .signer-role{font-size:7.3px;margin-top:3px}
  .letter-address{position:absolute;left:0;right:0;top:519px;text-align:center;font-family:"Lato",sans-serif;font-size:8.5px;color:#222}
  .letter-rule{position:absolute;left:71px;width:290px;top:533px;height:1px;background:var(--navy)}
  .letter-contacts{position:absolute;left:0;right:0;top:539px;display:flex;justify-content:center;gap:8px;font-family:"Lato",sans-serif;font-size:8.4px;color:#333;align-items:center}
  .contact{display:flex;align-items:center;gap:4px}
  .icon{width:13px;height:13px;flex:none}

  /* Envelope */
  .envelope-label{position:absolute;left:783px;top:125px;width:140px;text-align:center;font-family:"Lato",sans-serif;font-size:18px;color:var(--label)}
  .envelope{left:597px;top:171px;width:508px;height:229px}
  .envelope .wordmark{position:absolute;left:22px;top:38px;font-size:20px}
  .envelope-rule{position:absolute;left:26px;width:427px;top:199px;height:1px;background:var(--navy)}
  .envelope-address{position:absolute;left:26px;top:204px;font-family:"Lato",sans-serif;font-size:9px;color:#222}

  /* Business cards */
  .card{top:487px;width:233px;height:138px}
  .card-front{left:608px}
  .card-front .wordmark{position:absolute;right:18px;top:22px;font-size:12.5px;gap:4px}
  .card-front .wordmark .dot{width:7px;height:7px}
  .card-name{position:absolute;left:13px;top:70px;font-family:"Lato",sans-serif;font-weight:700;font-size:8.4px;color:var(--navy)}
  .card-role{position:absolute;left:13px;top:80px;font-family:"Lato",sans-serif;font-size:6.4px;color:var(--muted)}
  .card-rule{position:absolute;left:73px;right:20px;top:84px;height:1px;background:var(--navy)}
  .card-contacts{position:absolute;left:12px;top:100px;font-family:"Lato",sans-serif;font-size:6.2px;color:var(--muted);line-height:8.8px}
  .card-contacts .contact{gap:3px}
  .card-contacts .icon{width:8px;height:8px}
  .card-address{position:absolute;right:20px;top:111px;text-align:right;font-family:"Lato",sans-serif;font-size:6.2px;line-height:8.5px;color:var(--muted)}
  .card-back{left:863px;background:var(--navy)}
  .card-back .wordmark{position:absolute;left:0;right:0;top:61px;justify-content:center;color:var(--paper);font-size:14px}
  .card-back .wordmark .dot{background:var(--paper);width:8px;height:8px}
</style>
</head>
<body>

<svg width="0" height="0" style="position:absolute">
  <defs>
    <symbol id="i-phone" viewBox="0 0 16 16"><circle cx="8" cy="8" r="8" fill="#1e3766"/><path d="M5.2 4.2c.4-.3.9-.2 1.1.2l.6 1.2c.2.4 0 .8-.3 1l-.4.3c.4.9 1.1 1.6 2 2l.3-.4c.2-.3.7-.5 1-.3l1.2.6c.4.2.5.7.2 1.1l-.5.6c-.4.4-1 .5-1.5.3C6.9 10 5.9 9 5.2 7.1c-.2-.5-.1-1.1.3-1.5z" fill="#fff"/></symbol>
    <symbol id="i-mail" viewBox="0 0 16 16"><circle cx="8" cy="8" r="8" fill="#1e3766"/><rect x="4" y="5.2" width="8" height="5.6" fill="none" stroke="#fff" stroke-width="1"/><path d="M4 5.4l4 3 4-3" fill="none" stroke="#fff" stroke-width="1"/></symbol>
    <symbol id="i-web" viewBox="0 0 16 16"><circle cx="8" cy="8" r="8" fill="#1e3766"/><circle cx="8" cy="8" r="4" fill="none" stroke="#fff" stroke-width="1"/><path d="M4 8h8M8 4c-1.6 2.4-1.6 5.6 0 8M8 4c1.6 2.4 1.6 5.6 0 8" fill="none" stroke="#fff" stroke-width=".8"/></symbol>
  </defs>
</svg>

<!-- Letterhead -->
<section class="sheet letterhead">
  <div class="wordmark"><span class="dot"></span>Quillmark Select</div>

  <div class="letter-body letter-meta">
    <p>Issuing Date: May 5, 2018</p>
    <p>Name Of Employee Mr. Hartwell<br>Address of Employee<br>Address Line 2 etc..</p>
    <p class="salutation">Dear Mr.Hartwell</p>
  </div>

  <div class="letter-body letter-text">
    <p>Lorem Ipsum has been the industry's standard dummy text ever since the 1500s, when an unknown printer took a galley of type and scrambled it to make a type specimen book. It has survived not only five centuries, but also the leap into electronic typesetting, remaining essentially unchanged. It was popularised in the 1960s with the release of Brightline sheets containing Lorem Ipsum passages, and more recently with desktop publishing software like Pressworks Studio.</p>
    <p>Lorem Ipsum is simply dummy text of the printing and typesetting industry. Lorem Ipsum has been the industry's standard dummy text ever since the 1500s, when an unknown printer took a galley of type and scrambled it to make a type specimen book.</p>
    <p>It has survived not only five centuries, but also the leap into electronic typesetting, remaining essentially unchanged. It was popularised in the 1960s with the release of Brightline sheets containing Lorem Ipsum passages.</p>
  </div>

  <div class="closing">
    <p>Yours Sincerely</p>
    <span class="signature" role="img" aria-label="Handwritten signature of Dorian Velasco"></span>
    <p class="signer-name">Dorian Velasco</p>
    <p class="signer-role">Managing Director</p>
  </div>

  <p class="letter-address">88, Orchard Field Road Brookvale, 30817</p>
  <div class="letter-rule"></div>
  <div class="letter-contacts">
    <span class="contact"><svg class="icon"><use href="#i-phone"/></svg>031-555 208 417</span>
    <span class="contact"><svg class="icon"><use href="#i-mail"/></svg>hello@quillmarkselect.org</span>
    <span class="contact"><svg class="icon"><use href="#i-web"/></svg>www.quillmarkselect.org</span>
  </div>
</section>

<!-- Envelope -->
<p class="envelope-label">Envelope</p>
<section class="sheet envelope">
  <div class="wordmark"><span class="dot"></span>Quillmark Select</div>
  <div class="envelope-rule"></div>
  <p class="envelope-address">88, Orchard Field Road Brookvale, 30817</p>
</section>

<!-- Business card front -->
<section class="sheet card card-front">
  <div class="wordmark"><span class="dot"></span>Quillmark Select</div>
  <p class="card-name">DORIAN VELASCO</p>
  <p class="card-role">Managing Director</p>
  <div class="card-rule"></div>
  <div class="card-contacts">
    <div class="contact"><svg class="icon"><use href="#i-phone"/></svg>031-555 208 417</div>
    <div class="contact"><svg class="icon"><use href="#i-mail"/></svg>hello@quillmarkselect.org</div>
    <div class="contact"><svg class="icon"><use href="#i-web"/></svg>www.quillmarkselect.org</div>
  </div>
  <p class="card-address">88, Orchard Field Road<br>Brookvale, 30817</p>
</section>

<!-- Business card back -->
<section class="sheet card card-back">
  <div class="wordmark"><span class="dot"></span>Quillmark Select</div>
</section>

</body>
</html>
```